Briney Lark Fare landing page design

We need a landing page designed for an ecommerce website that sales fresh US domestic shrimp from the Gulf of Mexico and ships them direct to the consumer "From Our Shore To Your Door". For the landing page, we would like customers to be able to place an order and or inquire further about our product as well as links to social media. The company logo is attached

1 page

```html
<!DOCTYPE html>
<html lang="en">
<head>
<meta charset="utf-8">
<title>Briney Lark Fare — Place an Order</title>
<link rel="stylesheet" href="https://fonts.googleapis.com/css2?family=Montserrat:ital,wght@0,400;0,500;0,700;1,400;1,700&family=Arimo:ital@0;1&display=swap">
<style>
  :root {
    --header-teal: #326c87;
    --header-shadow: #2a5d75;
    --tagline: #d4e3ea;
    --connect: #1f3f4f;
    --icon-line: #e4eef2;
    --card-bg: rgba(255, 255, 255, 0.88);
    --ink: #444444;
    --field-ink: #333333;
    --field-border: #4a4a4a;
    --button: #366d87;
    --white: #ffffff;
  }
  * { box-sizing: border-box; margin: 0; padding: 0; }
  html, body { width: 1200px; height: 684px; overflow: hidden; }
  body { position: relative; font-family: "Montserrat", sans-serif; background: #c96a45; }

  .hero-photo {
    position: absolute; inset: 70px 0 0 0;
    background:
      radial-gradient(ellipse 30% 40% at 95% 35%, rgba(58, 95, 52, 0.9), rgba(58, 95, 52, 0) 70%),
      radial-gradient(ellipse 70% 60% at 40% 45%, #f2a07a, rgba(242, 160, 122, 0) 80%),
      linear-gradient(180deg, #e98f67 0%, #e58a63 55%, #a85a3c 85%, #5a3426 100%);
  }

  .site-header {
    position: absolute; top: 0; left: 0; width: 1200px; height: 70px;
    background: var(--header-teal);
    box-shadow: 0 1px 2px var(--header-shadow);
  }
  .brand {
    position: absolute; left: 182px; top: 10px; height: 48px;
    display: flex; align-items: center; gap: 10px;
  }
  .brand-dot { width: 46px; height: 46px; border-radius: 50%; border: 2px solid #1c3a48; }
  .brand-name {
    font-weight: 500; font-size: 17px; letter-spacing: 3px;
    color: #1c2a30; text-transform: uppercase; line-height: 1.1; width: 140px;
  }
  .tagline {
    position: absolute; left: 392px; width: 400px; top: 21px;
    text-align: center; font-style: italic; font-size: 22px; color: var(--tagline);
  }
  .tagline strong { font-weight: 700; }
  .social {
    position: absolute; left: 818px; top: 8px; width: 118px; text-align: center;
  }
  .social-label { font-size: 11px; color: var(--connect); display: block; margin-left: 18px; }
  .social-links { display: flex; gap: 12px; margin-top: 7px; justify-content: flex-start; padding-left: 2px; }
  .social-links a {
    width: 18px; height: 18px; border-radius: 50%;
    border: 1.3px solid var(--icon-line); display: block;
  }

  .order-card {
    position: absolute; left: 391px; top: 146px; width: 405px; height: 392px;
    background: var(--card-bg);
    box-shadow: 0 1px 3px rgba(0,0,0,0.2);
  }
  .order-title {
    margin-top: 34px; text-align: center; font-weight: 400;
    font-size: 30px; color: var(--ink); letter-spacing: 0.5px;
  }
  .divider {
    margin: 17px auto 0; width: 319px; border-top: 2px dotted #555;
  }
  .order-form { margin-top: 22px; }
  .field { position: relative; height: 37px; margin-bottom: 25px; }
  .field svg { position: absolute; left: 49px; top: 6px; width: 24px; height: 24px; fill: #3a3a3a; }
  .field input {
    position: absolute; left: 89px; width: 267px; height: 37px;
    border: 1px solid var(--field-border); background: transparent;
    padding-left: 14px; font-family: "Arimo", sans-serif; font-style: italic;
    font-size: 19px; color: var(--field-ink);
  }
  .field input::placeholder { color: var(--field-ink); opacity: 1; }
  .order-button {
    position: absolute; left: 143px; top: 301px; width: 120px; height: 39px;
    background: var(--button); color: var(--white); border: none;
    font-family: "Arimo", sans-serif; font-size: 19px;
    box-shadow: 0 1px 2px rgba(0,0,0,0.3);
  }
</style>
</head>
<body>
  <div class="hero-photo" role="img" aria-label="Close-up photograph of a heaped plate of cooked Gulf shrimp beside fresh dill"></div>

  <header class="site-header">
    <div class="brand">
      <span class="brand-dot"></span>
      <span class="brand-name">Briney Lark Fare</span>
    </div>
    <p class="tagline">“From our <strong>shore</strong>, to your <strong>door</strong>.”</p>
    <nav class="social" aria-label="Social media">
      <span class="social-label">connect</span>
      <div class="social-links">
        <a href="#" aria-label="Social profile 1"></a>
        <a href="#" aria-label="Social profile 2"></a>
        <a href="#" aria-label="Social profile 3"></a>
        <a href="#" aria-label="Social profile 4"></a>
      </div>
    </nav>
  </header>

  <main class="order-card">
    <h1 class="order-title">PLACE AN ORDER</h1>
    <div class="divider"></div>
    <form class="order-form">
      <div class="field">
        <svg viewBox="0 0 24 24" aria-hidden="true"><circle cx="12" cy="7" r="5"/><path d="M2 24v-4c0-4 4-7 10-7s10 3 10 7v4z"/></svg>
        <input type="text" placeholder="full name">
      </div>
      <div class="field">
        <svg viewBox="0 0 24 24" aria-hidden="true"><path d="M0 4h24v3l-12 7L0 7z"/><path d="M0 10l12 7 12-7v11H0z"/></svg>
        <input type="email" placeholder="email address" style="left:90px">
      </div>
      <div class="field">
        <svg viewBox="0 0 24 24" aria-hidden="true"><path d="M5 1l4 5-2.5 3c1.5 3.5 4 6 8.5 8.5l3-2.5 5 4-3 4C10 22 2 14 1 4z"/></svg>
        <input type="tel" placeholder="phone number">
      </div>
      <button class="order-button" type="submit">ORDER</button>
    </form>
  </main>
</body>
</html>
```